Grand Opening for Brightvale Church

Would like to have a BillBoard Created according to the specs listed by the company who will be producing the print. I am attaching the spec sheet to this post. I am also attaching a couple different picture options as well as a former Billboard design that was done. I would like the design to incorporate my logo, picture. I am okay if the background on the picture is eliminated for creative purposes. The words to be displayed is "Grand Opening" April 12, 2020 at the former Halden Middle School) 71st Marsh Hollow Rd.

Colors

Designer to choose colors to be used in the design.

Requirements
Must have
• Something that pops
Nice to have
• Good color coordinations and clearly visible text

```html
<!DOCTYPE html>
<html lang="en">
<head>
<meta charset="UTF-8">
<title>Brightvale Church – Grand Opening Billboard</title>
<link rel="stylesheet" href="https://fonts.googleapis.com/css2?family=Arimo:wght@700&display=swap">
<style>
  :root {
    --stage: #e8e6e4;
    --board: #3a1e1f;
    --board-deep: #2f1718;
    --glow: #ffffff;
    --ink-light: #ffffff;
    --ink-dark: #2a1c1c;
    --accent: #ee8a24;
    --jacket: #9a5626;
    --shirt: #e8d2cc;
  }
  * { margin: 0; padding: 0; box-sizing: border-box; }
  html, body {
    width: 1200px;
    height: 839px;
    overflow: hidden;
    background: var(--stage);
  }
  .billboard {
    position: absolute;
    left: 0;
    top: 143px;
    width: 1200px;
    height: 552px;
    background: var(--board);
    overflow: hidden;
    font-family: "Arimo", Arial, sans-serif;
    font-weight: 700;
  }
  .brand-glow {
    position: absolute;
    left: -160px;
    top: -200px;
    width: 800px;
    height: 500px;
    background: radial-gradient(ellipse at 38% 52%, rgba(255,255,255,0.97) 0%, rgba(255,255,255,0.8) 25%, rgba(200,180,180,0.35) 48%, rgba(58,30,31,0) 68%);
  }
  .brand {
    position: absolute;
    left: 24px;
    top: 104px;
    display: flex;
    align-items: center;
    gap: 14px;
  }
  .brand-dot {
    width: 30px;
    height: 30px;
    border-radius: 50%;
    background: var(--accent);
  }
  .brand-name {
    font-size: 40px;
    color: var(--ink-dark);
    letter-spacing: 0.5px;
  }
  .rule {
    position: absolute;
    left: 0;
    width: 690px;
    height: 3px;
    background: linear-gradient(90deg, rgba(255,255,255,0.85) 0%, rgba(255,255,255,0.75) 70%, rgba(255,255,255,0) 100%);
  }
  .rule--top { top: 248px; }
  .rule--bottom { top: 361px; }
  .headline {
    position: absolute;
    left: 37px;
    top: 265px;
    font-size: 78px;
    line-height: 1;
    color: var(--ink-light);
    letter-spacing: 0.5px;
    text-shadow: 0 3px 4px rgba(0,0,0,0.55);
    white-space: nowrap;
  }
  .event-date {
    position: absolute;
    left: 0;
    width: 694px;
    top: 390px;
    text-align: center;
    font-size: 54px;
    line-height: 1;
    color: var(--ink-light);
    word-spacing: 12px;
    text-shadow: 0 3px 4px rgba(0,0,0,0.55);
    white-space: nowrap;
  }
  .venue {
    position: absolute;
    left: 0;
    width: 694px;
    top: 467px;
    text-align: center;
    font-size: 27px;
    line-height: 33px;
    color: var(--ink-light);
    text-shadow: 0 2px 3px rgba(0,0,0,0.55);
  }
  .pastor-photo {
    position: absolute;
    left: 720px;
    top: 34px;
    width: 460px;
    height: 518px;
    background: linear-gradient(100deg, rgba(154,86,38,0) 0%, var(--jacket) 30%, var(--shirt) 55%, var(--jacket) 72%, rgba(154,86,38,0.2) 100%);
    opacity: 0.85;
    border-radius: 46% 46% 0 0 / 30% 30% 0 0;
  }
</style>
</head>
<body>
  <main class="billboard">
    <div class="brand-glow"></div>
    <div class="brand">
      <span class="brand-dot"></span>
      <span class="brand-name">Brightvale Church</span>
    </div>

    <div class="rule rule--top"></div>
    <h1 class="headline">GRAND OPENING</h1>
    <div class="rule rule--bottom"></div>

    <p class="event-date">April 12 2020 10 AM</p>
    <p class="venue">at the former Halden Middle School<br>71st Marsh Hollow Rd.</p>

    <div class="pastor-photo" role="img" aria-label="Photo of the pastor speaking with open hands, wearing a brown corduroy jacket and striped shirt"></div>
  </main>
</body>
</html>
```